Website design that will showcase a medical assistance tool

I want the medical assistance tool (for hearing aids) website to have a premium or upmarket feel. The brand is Plivoran (as per attached logo image for guidance). I want the website to appeal to both end users as well as hearing aid clinics.

```html
<!DOCTYPE html>
<html lang="en">
<head>
<meta charset="utf-8">
<title>Plivoran — Hearing Aid Comfort &amp; Care</title>
<link href="https://fonts.googleapis.com/css2?family=Montserrat:wght@300;400;500;600;700&display=swap" rel="stylesheet">
<style>
:root{
  --cream:#f4f0e3;
  --tan:#c9bfa4;
  --tan-dark:#b5aa8c;
  --ink:#2a2a2a;
  --muted:#6b6b66;
  --white:#ffffff;
  --grey:#ececeb;
}
*{box-sizing:border-box;margin:0;padding:0}
html,body{width:1200px;height:4605px;overflow:hidden}
body{position:relative;font-family:"Montserrat",sans-serif;color:var(--ink);background:var(--white)}
.abs{position:absolute}
.eyebrow{font-size:15px;letter-spacing:4px;text-transform:uppercase;font-weight:500}
.h2{font-size:40px;font-weight:400;line-height:1.2}
.body-text{font-size:16px;line-height:25px}
.btn{display:flex;align-items:center;justify-content:center;background:var(--tan);color:var(--white);border-radius:30px;font-size:13px;font-weight:600;letter-spacing:1px;text-transform:uppercase}
.photo{background:linear-gradient(135deg,#e7e2d6,#bfb6a2)}

/* nav */
.nav{left:75px;top:14px;width:1048px;height:72px;background:var(--white);border-radius:36px;box-shadow:0 4px 18px rgba(0,0,0,.05);display:flex;align-items:center;padding:0 24px}
.brand{display:flex;align-items:center;gap:8px;font-size:34px;font-weight:400;color:var(--ink)}
.brand-dot{width:34px;height:34px;border-radius:50%;background:var(--tan)}
.nav-links{display:flex;gap:44px;margin-left:76px;font-size:13px;font-weight:500}
.nav-contact{margin-left:44px;width:104px;height:30px;font-size:12px;text-transform:none;letter-spacing:0;font-weight:500}
.socials{display:flex;gap:6px;margin-left:28px}
.social{width:22px;height:22px;border-radius:50%;background:var(--muted)}

/* hero */
.hero{left:0;top:0;width:1200px;height:740px;background:var(--cream)}
.hero-title{left:93px;top:240px;font-size:46px;font-weight:500;line-height:48px}
.hero-text{left:93px;top:400px;width:400px;font-size:16px;line-height:25px}
.hero-btn{left:98px;top:477px;width:215px;height:50px;font-size:15px}

/* features */
.feature{top:813px;width:254px;height:215px;border:2px solid #e3ddcc;background:var(--white);text-align:center;padding-top:36px}
.feature.active{background:var(--tan);border-color:var(--tan);color:var(--white);top:797px;height:246px;padding-top:52px}
.feature-icon{width:46px;height:46px;border:2px solid var(--tan-dark);border-radius:50%;margin:0 auto 18px}
.feature.active .feature-icon{border-color:var(--white)}
.feature h3{font-size:18px;font-weight:600;line-height:22px}
.feature hr{width:30px;border:0;border-top:2px solid var(--tan);margin:10px auto}
.feature.active hr{border-color:var(--white)}
.feature p{font-size:12px;line-height:15px;color:var(--muted)}
.feature.active p{color:var(--white)}

/* benefits */
.benefits{left:0;top:1659px;width:1200px;height:737px;background:var(--cream)}
.bcard{top:1817px;width:409px;height:459px;background:var(--white);box-shadow:0 6px 20px rgba(0,0,0,.06)}
.bcard .photo{height:241px}
.bcard h3{font-size:21px;font-weight:600;margin:34px 0 0 58px}
.bcard hr{width:36px;border:0;border-top:2px solid var(--tan);margin:12px 0 14px 58px}
.bcard ul{list-style:none;margin-left:58px}
.bcard li{font-size:14px;font-weight:500;line-height:28px;display:flex;align-items:center;gap:8px}
.tick{width:14px;height:14px}

/* how */
.how{left:0;top:3022px;width:1200px;height:559px;background:var(--grey)}
.step{width:330px;height:330px;border-radius:50%;background:var(--white);box-shadow:0 0 0 8px #f6f6f4;text-align:center;padding:60px 40px 0}
.step.active{background:var(--tan);color:var(--white);box-shadow:0 0 0 8px #ddd6c4}
.step .num{font-size:60px;font-weight:300;color:var(--tan)}
.step.active .num{color:var(--white)}
.step h4{font-size:14px;font-weight:600;margin:8px 0 6px}
.step p{font-size:13px;line-height:21px}

/* testimonials */
.tside{top:3828px;width:160px;height:190px;background:#f5f5f3}
.tside p{font-size:10px;line-height:14px;color:#c4c4bf;text-align:center;padding:50px 14px}
.tmain{left:275px;top:3782px;width:642px;height:277px;background:var(--tan);color:var(--white);text-align:center;padding:78px 50px 0}
.tmain p{font-size:17px;line-height:25px}
.tmain .name{font-weight:600;margin-top:16px;font-size:16px}
.avatar{left:546px;top:3746px;width:98px;height:98px;border-radius:50%;border:4px solid var(--white)}
.arrow{top:4085px;width:42px;height:42px;border-radius:50%;background:var(--tan);display:flex;align-items:center;justify-content:center}

/* footer */
.footer{left:0;top:4166px;width:1200px;height:439px;background:var(--cream)}
.fcol h4{font-size:18px;font-weight:600;margin-bottom:18px}
.fcol a,.fcol span{display:block;font-size:12px;line-height:23px;color:var(--ink);text-decoration:none}
.contact-row{display:flex;gap:12px;align-items:center;margin-bottom:18px;font-size:11px;line-height:14px}
.cicon{width:26px;height:26px;border-radius:50%;background:var(--tan);flex:none}
</style>
</head>
<body>

<!-- hero -->
<section class="abs hero">
  <svg class="abs" style="left:0;top:600px" width="1200" height="140" viewBox="0 0 1200 140">
    <path d="M0 80 C180 150 360 120 520 90 C700 50 900 30 1200 60 L1200 140 L0 140Z" fill="#ffffff"/>
    <path d="M0 80 C180 150 360 120 520 90 C700 50 900 30 1200 60" fill="none" stroke="var(--tan)" stroke-width="10"/>
  </svg>
  <div class="abs photo" role="img" aria-label="Smiling older woman with grey hair touching a hearing aid behind her ear" style="left:733px;top:116px;width:467px;height:560px;background:linear-gradient(160deg,#efeadc 0%,#d8d2c4 55%,#f2eee3 100%);border-radius:0 0 0 40px"></div>
  <div class="abs" role="img" aria-label="Champagne-gold behind-the-ear hearing aid with clear tube and ear dome" style="left:468px;top:483px;width:184px;height:241px;border-radius:60px;background:linear-gradient(135deg,#e8dfc4,#b6a478)"></div>
  <div class="abs eyebrow" style="left:94px;top:218px">Welcome to Plivoran</div>
  <h1 class="abs hero-title">A New Standard<br>in Hearing Aid<br>Comfort &amp; Care</h1>
  <p class="abs hero-text">Lorem ipsum dolor sit amet, consectetur adipiscing elit sed do eiusmod tempor incididunt</p>
  <div class="abs btn hero-btn">Try it now →</div>
</section>

<nav class="abs nav">
  <div class="brand"><span class="brand-dot"></span>plivoran</div>
  <div class="nav-links"><span>Home</span><span>For Individuals</span><span>For Clinics</span><span>About</span><span>Support</span></div>
  <div class="btn nav-contact">Contact</div>
  <div class="socials"><span class="social"></span><span class="social"></span><span class="social"></span></div>
</nav>

<!-- features -->
<div class="abs feature" style="left:93px"><div class="feature-icon"></div><h3>Premium Comfort</h3><hr><p>Lorem ipsum dolor sit amet,<br>consectetur adipiscing</p></div>
<div class="abs feature active" style="left:361px"><div class="feature-icon"></div><h3>Clinically Trusted</h3><hr><p>Lorem ipsum dolor sit amet,<br>consectetur adipiscing</p></div>
<div class="abs feature" style="left:626px"><div class="feature-icon"></div><h3>Easy to use &amp; Hygienic</h3><hr><p>Lorem ipsum dolor sit amet,<br>consectetur adipiscing</p></div>
<div class="abs feature" style="left:890px;padding-top:28px"><div class="feature-icon"></div><h3>Improves Patient<br>Experience</h3><hr><p>Lorem ipsum dolor sit amet,<br>consectetur adipiscing</p></div>

<!-- about -->
<div class="abs" style="left:84px;top:1095px;width:466px;height:466px;border-radius:50%;background:var(--tan)"></div>
<div class="abs photo" role="img" aria-label="Smiling older man with white beard fitting a hearing aid" style="left:104px;top:1115px;width:440px;height:440px;border-radius:50%;background:linear-gradient(135deg,#f0ece2,#a9a290)"></div>
<div class="abs eyebrow" style="left:594px;top:1145px">About Plivoran</div>
<h2 class="abs h2" style="left:590px;top:1172px">About the Technology</h2>
<div class="abs" style="left:1048px;top:1182px;width:38px;height:38px;border-radius:50%;border:5px solid var(--tan)"></div>
<p class="abs body-text" style="left:592px;top:1244px;width:510px">Lorem ipsum dolor sit amet, consectetur adipiscing elit, sed do eiusmod tempor incididunt ut labore et dolore magna aliqua. Quis ipsum suspendisse ultrices gravida. Risus commodo viverra maecenas accumsan lacus vel facilisis.</p>
<p class="abs body-text" style="left:592px;top:1369px;width:510px">Lorem ipsum dolor sit amet, consectetur adipiscing elit, sed do eiusmod tempor incididunt ut labore et dolore magna aliqua. Quis ipsum suspendisse ultrices gravida.</p>
<div class="abs btn" style="left:594px;top:1471px;width:164px;height:42px">Learn more</div>

<!-- benefits -->
<section class="abs benefits"></section>
<div class="abs" style="left:564px;top:1628px;width:70px;height:70px;border-radius:50%;background:var(--white)"></div>
<div class="abs eyebrow" style="left:0;width:1200px;text-align:center;top:1706px">Why choose us</div>
<h2 class="abs h2" style="left:0;width:1200px;text-align:center;top:1728px">Benefits &amp; Features</h2>
<div class="abs bcard" style="left:179px">
  <div class="photo" role="img" aria-label="Smiling woman with glasses touching her ear outdoors"></div>
  <h3>FOR END USERS</h3><hr>
  <ul>
    <li><svg class="tick" viewBox="0 0 14 14"><path d="M2 7l3 3 7-7" fill="none" stroke="var(--tan)" stroke-width="2"/></svg>Comfort</li>
    <li><svg class="tick" viewBox="0 0 14 14"><path d="M2 7l3 3 7-7" fill="none" stroke="var(--tan)" stroke-width="2"/></svg>Hygiene</li>
    <li><svg class="tick" viewBox="0 0 14 14"><path d="M2 7l3 3 7-7" fill="none" stroke="var(--tan)" stroke-width="2"/></svg>Ease of use</li>
    <li><svg class="tick" viewBox="0 0 14 14"><path d="M2 7l3 3 7-7" fill="none" stroke="var(--tan)" stroke-width="2"/></svg>Improved experience</li>
  </ul>
</div>
<div class="abs bcard" style="left:606px">
  <div class="photo" role="img" aria-label="Clinician fitting a hearing aid to a bearded man" style="background:linear-gradient(135deg,#d9d3c7,#8c8272)"></div>
  <h3>FOR CLINICS</h3><hr>
  <ul>
    <li><svg class="tick" viewBox="0 0 14 14"><path d="M2 7l3 3 7-7" fill="none" stroke="var(--tan)" stroke-width="2"/></svg>Increased patient satisfaction</li>
    <li><svg class="tick" viewBox="0 0 14 14"><path d="M2 7l3 3 7-7" fill="none" stroke="var(--tan)" stroke-width="2"/></svg>Reduced follow-up issues</li>
    <li><svg class="tick" viewBox="0 0 14 14"><path d="M2 7l3 3 7-7" fill="none" stroke="var(--tan)" stroke-width="2"/></svg>Premium positioning</li>
  </ul>
</div>

<!-- technology -->
<div class="abs photo" role="img" aria-label="Laughing woman with short grey hair having a hearing aid fitted" style="left:536px;top:2396px;width:664px;height:626px;background:linear-gradient(90deg,#ffffff 0%,#ece7dc 40%,#c9b9a4 100%)"></div>
<svg class="abs" style="left:0;top:2320px" width="1200" height="110" viewBox="0 0 1200 110">
  <path d="M0 60 C200 110 380 40 560 50 C760 60 900 10 1200 40 L1200 0 L0 0Z" fill="var(--cream)"/>
  <path d="M0 60 C200 110 380 40 560 50 C760 60 900 10 1200 40" fill="none" stroke="var(--tan)" stroke-width="8"/>
</svg>
<div class="abs eyebrow" style="left:126px;top:2533px">Why choose us</div>
<h2 class="abs h2" style="left:125px;top:2560px;line-height:48px">Technology &amp; <span style="display:inline-block;width:36px;height:36px;border-radius:50%;border:5px solid var(--tan);vertical-align:-4px"></span><br>Design Excellence</h2>
<p class="abs body-text" style="left:133px;top:2670px;width:420px">Lorem ipsum dolor sit amet, consectetur adipiscing elit, sed do eiusmod tempor incididunt ut labore et dolore magna aliqua Quis ipsum suspe</p>
<p class="abs body-text" style="left:133px;top:2770px;width:420px">Lorem ipsum dolor sit amet, consectetur adipiscing elit, sed do eiusmod tempor incididunt.</p>
<div class="abs btn" style="left:133px;top:2848px;width:163px;height:42px">Learn more</div>

<!-- how it works -->
<section class="abs how"></section>
<h2 class="abs h2" style="left:0;width:1200px;text-align:center;top:3080px">How it Works</h2>
<div class="abs step" style="left:143px;top:3164px"><div class="num">01</div><h4>Lorem ipsum dolor sit</h4><p>dipiscing elit, sed do eiusmod tempor incididunt ut labore et dolore magna aliqua. Quis ipsum sus-pendisse ultrices gravida</p></div>
<div class="abs step active" style="left:445px;top:3160px"><div class="num">02</div><h4>Lorem ipsum dolor sit</h4><p>dipiscing elit, sed do eiusmod tempor incididunt ut labore et dolore magna aliqua. Quis ipsum sus-pendisse ultrices gravida</p></div>
<div class="abs step" style="left:738px;top:3158px"><div class="num">03</div><h4>Lorem ipsum dolor sit</h4><p>dipiscing elit, sed do eiusmod tempor incididunt ut labore et dolore magna aliqua. Quis ipsum sus-pendisse ultrices gravida</p></div>

<!-- testimonials -->
<div class="abs eyebrow" style="left:0;width:1200px;text-align:center;top:3636px">Testimonials</div>
<h2 class="abs h2" style="left:0;width:1200px;text-align:center;top:3660px">What People are Saying</h2>
<div class="abs tside" style="left:120px"><p>"Lorem ipsum dolor sit amet, eiusmod tempor incid ipsum suspendisse maecenas"</p></div>
<div class="abs tside" style="left:910px"><p>adipiscing elit, sed do magna aliqua. Quis commodo viverra facilisis"</p></div>
<div class="abs tmain">
  <p>"Lorem ipsum dolor sit amet, consectetur adipiscing elit, sed do eiusmod tempor incididunt ut labore et dolore magna aliqua. Quis ipsum suspendisse ultrices gravida. Risus commodo viverra maecenas accumsan lacus vel facilisis"</p>
  <div class="name">Martin Hale</div>
  <div style="letter-spacing:4px;font-size:16px">★★★★★</div>
  <div class="abs" style="right:44px;bottom:24px;font-size:110px;line-height:60px;opacity:.45">”</div>
</div>
<div class="abs photo avatar" role="img" aria-label="Portrait of a smiling customer"></div>
<div class="abs arrow" style="left:551px"><svg width="14" height="14" viewBox="0 0 14 14"><path d="M9 2L4 7l5 5" fill="none" stroke="#fff" stroke-width="2"/></svg></div>
<div class="abs arrow" style="left:608px"><svg width="14" height="14" viewBox="0 0 14 14"><path d="M5 2l5 5-5 5" fill="none" stroke="#fff" stroke-width="2"/></svg></div>

<!-- footer -->
<section class="abs footer"></section>
<svg class="abs" style="left:0;top:4130px" width="1200" height="90" viewBox="0 0 1200 90">
  <path d="M0 40 C200 10 420 70 620 60 C820 50 1000 20 1200 50 L1200 0 L0 0Z" fill="#ffffff"/>
  <path d="M0 40 C200 10 420 70 620 60 C820 50 1000 20 1200 50" fill="none" stroke="var(--tan)" stroke-width="8"/>
</svg>
<div class="abs brand" style="left:134px;top:4266px"><span class="brand-dot"></span>plivoran</div>
<p class="abs" style="left:140px;top:4326px;width:240px;font-size:11px;line-height:18px">Lorem ipsum dolor sit amet, consectetur adipiscing elit, sed do eiusmod tempor</p>
<div class="abs socials" style="left:140px;top:4382px;margin:0"><span class="social" style="width:28px;height:28px"></span><span class="social" style="width:28px;height:28px;background:var(--tan)"></span><span class="social" style="width:28px;height:28px;background:var(--tan)"></span><span class="social" style="width:28px;height:28px;background:var(--tan)"></span></div>
<div class="abs fcol" style="left:413px;top:4276px"><h4>Navigation</h4><a>Home</a><a>For Individuals</a><a>For Clinics</a><a>About</a><a>Support</a><a>Contact</a></div>
<div class="abs fcol" style="left:599px;top:4276px;width:240px"><h4>Contact us</h4>
  <div class="contact-row"><span class="cicon"></span><span style="font-size:11px;line-height:14px">48 Meridian Row<br>Suite 12, Leeds, UK LS1 4QT</span></div>
  <div class="contact-row"><span class="cicon"></span><span style="font-size:11px">+44 (0)113 555 0192</span></div>
  <div class="contact-row"><span class="cicon"></span><span style="font-size:11px">hello@plivoran.com</span></div>
</div>
<div class="abs fcol" style="left:890px;top:4276px"><h4>Subscribe Newletter</h4>
  <div style="width:204px;height:30px;border-radius:15px;background:#fff;font-size:10px;padding:9px 20px;color:var(--muted)">Email address</div>
  <div class="btn" style="width:204px;height:30px;margin-top:12px;font-size:11px;text-transform:none;font-weight:500">Subscribe ↗</div>
</div>
<div class="abs" style="left:134px;top:4524px;width:948px;border-top:1px solid #d8d1bd"></div>
<div class="abs" style="left:154px;top:4548px;font-size:12px">Copyright © 2025 plivoran. All Right Reserved</div>
<div class="abs" style="left:816px;top:4548px;font-size:12px;display:flex;gap:14px"><span>Terms of Use</span><span>Privacy Policy</span><span>Disclaimer</span></div>

</body>
</html>
```